Landfill Gas-to-Renewable Natural Gas business

We have a website ( corvelmetharoutes .com via Net Burrow) that needs to be revamped.

We have three RNG projects in Puerto Rico (Humacao, Ponce, Salinas), that take landfill gas (LFG) and produce renewable liquid natural gas (R-LNG) for companies looking to offset their carbon emissions (footprint). We also produce a renewable carbon dioxide (R-CO2) that can be reused for industrial CO2 purposes. All CO2 is imported to the island, so reusing CO2 on the island further reduces global CO2 emissions. The design should reflect renewables, sustainability, professionalism, safety and experience in this sector.

Sites with RNG examples:
https://www.qx.com/en_us/united-states/home/what-we-do/production-and-operations/tolvane-fuels.html
https://brambleflowco.com/
http://kessfordpower.com/operations/
https://wyndcastle.com/
https://www.tamberhold.com/
https://pexloweco.com/
https://sandmoorbiolines.com/
https://curvetto.com/
https://www.dolvatri.com/renewable-natural-gas/
https://www.haskipowerworks.com/

Renewables Natural Gas, Sustainability,

4 page

• Health, Safety, Environment (HSE) aspect. Industry experience section, about us, photos, landfill gas, LNG, RNG, CO2

```html
<!DOCTYPE html>
<html lang="en">
<head>
<meta charset="utf-8">
<title>Contact – Corvel Metharoutes</title>
<link rel="stylesheet" href="https://fonts.googleapis.com/css2?family=Inter:wght@400;500;600&display=swap">
<style>
:root{
  --green:#12d872;
  --ink:#1c1c1c;
  --muted:#8a8a8a;
  --line:#8f8f8f;
  --footer:#023f36;
  --footer-text:#d6e2de;
  --card:rgba(249,249,247,0.93);
  --brand:#24306b;
}
*{box-sizing:border-box;margin:0;padding:0}
html,body{width:1200px;height:1197px;overflow:hidden}
body{font-family:"Inter",sans-serif;color:var(--ink);background:#fff;position:relative}
.site-header{position:absolute;left:0;top:0;width:1200px;height:97px;background:#fff;z-index:2;box-shadow:0 2px 8px rgba(0,0,0,.05)}
.brand{position:absolute;left:67px;top:27px;display:flex;align-items:center;gap:10px;font-size:19px;color:var(--brand);text-decoration:none}
.brand-dot{width:40px;height:40px;border-radius:50%;background:var(--green)}
.main-nav{position:absolute;right:67px;top:25px;display:flex;align-items:center}
.main-nav a{font-size:14px;color:var(--ink);text-decoration:none;margin-left:36px}
.main-nav a:first-child{margin-left:0}
.btn{display:inline-flex;align-items:center;justify-content:center;gap:8px;background:var(--green);color:#fff;border-radius:24px;text-decoration:none;font-size:14px;border:0;font-family:inherit}
.main-nav .btn{width:135px;height:47px;margin-left:37px;color:#fff}
.hero{position:absolute;left:0;top:97px;width:1200px;height:800px;
  background:linear-gradient(180deg,#c9d0d2 0%,#d9d5c9 40%,#c7b99a 58%,#6d6a4e 72%,#4d4a36 100%)}
.card{position:absolute;left:261px;top:139px;width:678px;height:718px;background:var(--card);border-radius:6px;text-align:center}
.card h1{font-size:26px;font-weight:600;margin-top:40px}
.card .sub{font-size:18px;color:var(--muted);margin-top:10px}
.contact-form{position:absolute;left:139px;top:170px;width:387px;text-align:left}
.field{display:block;margin-bottom:25px}
.field span{display:block;font-size:15px;color:var(--muted)}
.field .input{height:10px;border-bottom:1px solid var(--line)}
.field.message span{margin-bottom:9px}
.field .textarea{height:152px;border:1px solid var(--line)}
.contact-form .btn{width:108px;height:46px;font-size:14px;position:absolute;left:139px;top:299px}
.legal{position:absolute;top:595px;left:0;width:100%;font-size:12px;color:var(--muted)}
.legal a,.footer-legal a{color:inherit}
.card .org{position:absolute;top:637px;left:0;width:100%;font-size:17px;font-weight:600;color:#9a9a9a}
.card .addr{position:absolute;top:663px;left:0;width:100%;font-size:14px;color:#9a9a9a}
.site-footer{position:absolute;left:0;top:897px;width:1200px;height:300px;background:var(--footer);color:var(--footer-text);font-size:14px}
.footer-legal{position:absolute;left:66px;top:60px;width:320px;line-height:16px}
.footer-legal p+p{margin-top:16px}
.footer-col{position:absolute;top:56px}
.footer-col h3{font-size:20px;font-weight:500;color:#fff;margin-bottom:17px}
.footer-col a{display:block;color:var(--footer-text);text-decoration:none;line-height:21px}
.copyright{position:absolute;left:66px;top:233px}
.social{position:absolute;right:67px;top:225px;display:flex;align-items:center;gap:9px}
.social span{margin-right:2px}
.social i{width:33px;height:33px;border:1px solid var(--footer-text);border-radius:50%;display:block}
</style>
</head>
<body>
<header class="site-header">
  <a class="brand" href="#"><span class="brand-dot"></span>Corvel Metharoutes</a>
  <nav class="main-nav">
    <a href="#">Home</a><a href="#">About</a><a href="#">FAQ</a>
    <a class="btn" href="#">Contact
      <svg width="10" height="10" viewBox="0 0 10 10" fill="none" stroke="#fff" stroke-width="1.4"><path d="M2 8L8 2M3 2h5v5"/></svg></a>
  </nav>
</header>

<section class="hero" role="img" aria-label="Photo of an engineer in a hard hat and safety vest looking toward wind turbines on a hillside at sunset">
</section>

<main class="card">
  <h1>Contact us</h1>
  <p class="sub">Drop us a line!</p>
  <form class="contact-form">
    <label class="field"><span>Name</span><div class="input"></div></label>
    <label class="field"><span>Email*</span><div class="input"></div></label>
    <label class="field message"><span>Message</span><div class="textarea"></div></label>
    <button class="btn" type="button">Send
      <svg width="10" height="10" viewBox="0 0 10 10" fill="none" stroke="#fff" stroke-width="1.4"><path d="M2 8L8 2M3 2h5v5"/></svg></button>
  </form>
  <p class="legal">This site is protected by BotGuard and the Vextra <a href="#">Privacy Policy</a> and <a href="#">Terms of Service</a> apply.</p>
  <p class="org">Corvel Metharoutes</p>
  <p class="addr">Urb. Vista Clara 148 Calle Marbella, Suite 210, San Juan, Puerto Rico 00907</p>
</main>

<footer class="site-footer">
  <div class="footer-legal">
    <p>This site is protected by BotGuard and the Vextra <a href="#">Privacy Policy</a> and <a href="#">Terms of Service</a> apply.</p>
    <p>Corvel Metharoutes<br>Urb. Vista Clara 148 Calle Marbella,<br>Suite 210, San Juan, Puerto Rico 00907</p>
  </div>
  <div class="footer-col" style="left:683px"><h3>About</h3><a href="#">Our Mission</a><a href="#">Our Services</a><a href="#">Our Team</a></div>
  <div class="footer-col" style="left:859px"><h3>FAQ</h3><a href="#" style="line-height:16px">Frequently<br>asked questions</a></div>
  <div class="footer-col" style="left:1058px"><h3>Contact</h3><a href="#">Contacts us</a></div>
  <p class="copyright">Corvel Metharoutes Website - All Rights Reserved. Copyright © 2025</p>
  <div class="social"><span>Follow us</span><i aria-label="Social profile"></i><i aria-label="Social profile"></i></div>
</footer>
</body>
</html>
```